Card for invoking rights with police

Our criminal defense law firm is seeking proposals for a design for our card intended for clients to carry with them in their car. Upon being pulled over, they would hand this card to the officer.
Text for the back of the card:
"For Law Enforcement:"
"I will comply with lawful orders but respectfully decline any test or other requests without my attorney. I wish to remain silent, do not consent to searches, and request to speak with my attorney now.
The back of the card should prominently feature the text and the firm logo should be secondary.
Front
Must prominently feature contact info: 425-600-3917. Do not include attorney name, email, phone from the example file. This is intended to be generic for the firm and not tied to an individual lawyer.
Included for design reference: current business card, firm logo.
We intend to use pliqo.example to produce the cards.
Updates
The back of the card should prominently display the text regarding invocation of rights. Please title it "For Law Enforcement".
Target Market(s)
People who have been stopped by police
Contact Information for Business Card
see project description
Look and feel
Each slider illustrates characteristics of the customer's brand and the style your logo design should communicate.

```html
<!DOCTYPE html>
<html lang="en">
<head>
<meta charset="utf-8">
<title>Brennan Law Firm – Rights Card</title>
<link rel="stylesheet" href="https://fonts.googleapis.com/css2?family=Montserrat:wght@400;500;600;700&display=swap">
<style>
  :root {
    --navy: #173a5c;
    --navy-deep: #102c48;
    --paper: #ffffff;
    --ink-grey: #4a4f55;
    --backdrop: #1e1f21;
  }
  * { box-sizing: border-box; margin: 0; padding: 0; }
  html, body { width: 1200px; height: 801px; overflow: hidden; }
  body {
    background: var(--backdrop);
    font-family: "Montserrat", sans-serif;
    display: flex;
    align-items: center;
    justify-content: center;
    gap: 40px;
  }
  .card {
    width: 540px;
    height: 310px;
    border-radius: 22px;
    position: relative;
    overflow: hidden;
  }

  /* Shared firm name block */
  .brand {
    display: flex;
    align-items: center;
    gap: 12px;
    font-weight: 500;
  }
  .brand-mark { width: 34px; height: 34px; background: currentColor; flex: none; }
  .brand-name { display: flex; flex-direction: column; align-items: center; }
  .brand-name .firm { font-size: 26px; letter-spacing: 9px; line-height: 1; }
  .brand-name .sub {
    font-size: 10px; letter-spacing: 2px; margin-top: 5px;
    display: flex; align-items: center; gap: 8px;
  }
  .brand-name .sub::before, .brand-name .sub::after {
    content: ""; width: 34px; height: 1px; background: currentColor;
  }

  /* Front */
  .card-front { background: var(--paper); color: var(--navy); }
  .card-front .brand { position: absolute; top: 32px; right: 36px; color: var(--navy); }
  .hotline {
    position: absolute; left: 36px; top: 112px;
    display: flex; align-items: center; gap: 12px;
  }
  .hotline svg { width: 26px; height: 26px; fill: var(--navy); flex: none; }
  .hotline .number {
    font-size: 34px; font-weight: 700; letter-spacing: 1px; line-height: 1;
    color: var(--navy);
  }
  .divider {
    position: absolute; left: 36px; right: 36px; top: 178px;
    height: 1px; background: var(--navy);
  }
  .web {
    position: absolute; left: 36px; top: 198px;
    display: flex; align-items: center; gap: 8px;
    font-size: 13px; color: var(--ink-grey);
  }
  .web svg { width: 12px; height: 12px; fill: var(--navy); flex: none; }
  .address {
    position: absolute; right: 36px; top: 196px;
    text-align: right; font-size: 12px; line-height: 20px; color: var(--ink-grey);
    font-style: normal;
  }

  /* Back */
  .card-back {
    background: linear-gradient(160deg, var(--navy) 0%, var(--navy-deep) 100%);
    color: var(--paper);
    display: flex; flex-direction: column; align-items: center;
    padding: 26px 34px 0;
  }
  .card-back .brand { color: var(--paper); gap: 10px; }
  .card-back .brand-mark { width: 26px; height: 26px; }
  .card-back .brand-name .firm { font-size: 18px; letter-spacing: 6px; }
  .card-back .brand-name .sub { font-size: 8px; letter-spacing: 2px; margin-top: 4px; }
  .card-back .brand-name .sub::before, .card-back .brand-name .sub::after { width: 22px; }
  .rights-title {
    margin-top: 26px;
    font-size: 20px; font-weight: 700; letter-spacing: 1.5px;
    text-transform: uppercase;
  }
  .rights {
    margin-top: 14px; text-align: center;
    font-size: 15px; line-height: 23px; font-weight: 500;
  }
</style>
</head>
<body>
  <section class="card card-front">
    <div class="brand">
      <span class="brand-mark"></span>
      <span class="brand-name"><span class="firm">BRENNAN</span><span class="sub">LAW FIRM</span></span>
    </div>
    <div class="hotline">
      <svg viewBox="0 0 12 12"><path d="M2 1h2.5l1 3-1.5 1a7 7 0 0 0 3 3l1-1.5 3 1V10a1 1 0 0 1-1 1A9 9 0 0 1 1 2a1 1 0 0 1 1-1z"/></svg>
      <span class="number">425-600-3917</span>
    </div>
    <div class="divider"></div>
    <p class="web">
      <svg viewBox="0 0 12 12"><path d="M6 0a6 6 0 1 0 0 12A6 6 0 0 0 6 0zm0 1.2a4.8 4.8 0 1 1 0 9.6 4.8 4.8 0 0 1 0-9.6zM1.5 5.4h9v1.2h-9z"/></svg>
      www.brennanlawfirm.example
    </p>
    <address class="address">
      1820 Harbor View Ave NE<br>
      Suite 210<br>
      Lakemont, WA 98011
    </address>
  </section>

  <section class="card card-back">
    <div class="brand">
      <span class="brand-mark"></span>
      <span class="brand-name"><span class="firm">BRENNAN</span><span class="sub">LAW FIRM</span></span>
    </div>
    <h2 class="rights-title">For Law Enforcement:</h2>
    <p class="rights">
      I will comply with lawful orders but respectfully decline any test or other
      requests without my attorney. I wish to remain silent, do not consent to
      searches, and request to speak with my attorney now.
    </p>
  </section>
</body>
</html>
```